pharmacy/travel clinic business card design

We need a business card for our new business called Merrow Travel Clinic and Pharmacy. Our primary focus is doing consultations for people before travelling internationally and providing vaccinations and prescriptions for them. While the business is considered a pharmacy, it has more the look and feel of a doctor's office. The design should communicate a professional and trustworthy feel. I have attached a copy of the logo we are going to be using.
Updates
Thanks for the submissions.  If you haven`t been eliminated you are one of the finalists.  Decision will likely be made tomorrow.

Target Market(s)
Customers, other health care professionals, travel agents
Industry/Entity Type
Clinic
Look and feel
Each slider illustrates characteristics of the customer's brand and the style your logo design should communicate.

```html
<!DOCTYPE html>
<html lang="en">
<head>
<meta charset="utf-8">
<title>Merrow Travel Clinic and Pharmacy – Business Card</title>
<link rel="stylesheet" href="https://fonts.googleapis.com/css2?family=Montserrat:wght@500&family=Arimo:wght@400;700&display=swap">
<style>
  :root {
    --backdrop: #f1eee8;
    --card: #ffffff;
    --brand-green: #7be41a;
    --brand-blue: #2e7fe6;
    --icon-blue-light: #5cc8f5;
    --contact-cyan: #72d9f2;
    --card-shadow: rgba(40, 30, 20, 0.35);
  }
  * { margin: 0; padding: 0; box-sizing: border-box; }
  html, body {
    width: 1200px; height: 1000px; overflow: hidden;
    background: var(--backdrop);
  }
  .canvas { position: relative; width: 1200px; height: 1000px; }
  .card {
    position: absolute; left: 266px; width: 669px; height: 433px;
    background: var(--card);
    box-shadow: 3px 4px 6px var(--card-shadow);
  }
  .card--front { top: 47px; }
  .card--back { top: 521px; }

  .brand {
    position: absolute; left: 112px; top: 130px;
    display: flex; align-items: flex-start; gap: 18px;
  }
  .brand__mark {
    width: 34px; height: 34px; border-radius: 50%;
    background: var(--brand-blue); margin-top: 12px; flex: none;
  }
  .brand__name {
    font-family: "Montserrat", sans-serif; font-weight: 500;
    font-size: 52px; line-height: 54px; color: var(--brand-green);
    letter-spacing: -0.5px;
  }

  .icons { position: absolute; left: 42px; top: 144px; display: flex; gap: 22px; align-items: center; }
  .icon { display: block; }
  .globe {
    width: 64px; height: 64px; border-radius: 50%;
    background: radial-gradient(circle at 35% 35%, #8fd0fb, #2f86e0 70%);
  }
  .holder {
    position: absolute; left: 304px; top: 160px;
    font-family: "Arimo", sans-serif; font-weight: 700;
    font-size: 29px; color: var(--brand-blue); letter-spacing: 0.3px;
  }
  .contact {
    position: absolute; left: 302px; top: 263px; list-style: none;
    font-family: "Arimo", sans-serif; font-size: 22px; line-height: 30.5px;
    color: var(--contact-cyan);
  }
  .contact__label { color: var(--brand-green); font-weight: 700; }
  .contact li:first-child { font-size: 24px; }
</style>
</head>
<body>
<div class="canvas">
  <section class="card card--front">
    <div class="brand">
      <span class="brand__mark" aria-hidden="true"></span>
      <div class="brand__name">Merrow<br>Travel Clinic<br>and Pharmacy</div>
    </div>
  </section>

  <section class="card card--back">
    <div class="icons">
      <svg class="icon" width="58" height="58" viewBox="0 0 58 58" aria-label="Medical cross">
        <defs>
          <linearGradient id="crossFill" x1="0" y1="0" x2="0" y2="1">
            <stop offset="0" stop-color="var(--icon-blue-light)"/>
            <stop offset="1" stop-color="var(--brand-blue)"/>
          </linearGradient>
        </defs>
        <path d="M20 0h18v20h20v18H38v20H20V38H0V20h20z" fill="url(#crossFill)"/>
      </svg>
      <svg class="icon" width="68" height="60" viewBox="0 0 68 60" aria-label="Aeroplane">
        <path fill="var(--brand-green)" d="M4 27h22L16 2h8l20 25h14c6 0 8 2 8 3s-2 3-8 3H44L24 58h-8l10-25H4L0 41h-4z M0 22l5 8-5 8z"/>
      </svg>
      <div class="globe" role="img" aria-label="Globe showing the world"></div>
    </div>
    <h1 class="holder">NAME NAME NAME</h1>
    <ul class="contact">
      <li><span class="contact__label">t:</span> XXXX XXX XXX</li>
      <li><span class="contact__label">e:</span> xxxxxxxx@xxxxxx.com</li>
      <li><span class="contact__label">w:</span> xxxxxxxx@xxxxxx.com</li>
    </ul>
  </section>
</div>
</body>
</html>
```